4-Page Brochure for Harbor Renewals

Harbor Renewals is a multi-faceted company established by a board certified
physician with over 20 years of experience. We assist our clients in naturally optimizing their wellness and appearance through a holistic approach which includes:(1) a personalized, medically-supervised weight loss program, (2) cosmetic body treatments such as lipolaser, cool sculpting, radio frequency and ultrasound cavitation, skin tightening, lifting. We can reduce double chin, acne scars, facial wrinkles and blemishes. Our state of the art machines can reduce cellulite. and skin dimpling physician-formulated vitamins, supplements, nutraceuticals and skin care products which will be offered in our medical offices and online nationally, and (4) vitamin and mineral-enhanced beverage products which will also be offered in our offices as well as online nationally. We want our improve the way our clients feel, as well as how they look.
Design Specifics: We think a design which in some way represents the human body/form would be most representative of our company's mission. We do not want to use pink, as our products and services are designed for both genders. Other than that, we are open to different color schemes. We wouldn't use flowery script-type or very informal fonts, but rather something more professional looking.
Target Market(s)
man and women age 30 Plus
Industry/Entity Type
It Company
Contact Information for Business Card
I have attached a logo of my company " Harbor Renewals: Card must have it
Requirements
Must have
- Logo that I submitted,

```html
<!DOCTYPE html>
<html lang="en">
<head>
<meta charset="UTF-8">
<title>Harbor Renewals – Flyer</title>
<link href="https://fonts.googleapis.com/css2?family=Montserrat:wght@400;700&family=Roboto+Condensed:wght@700&family=PT+Sans:wght@400;700&family=Arimo:wght@400;700&display=swap" rel="stylesheet">
<style>
  :root{
    --purple:#6e3c8c;
    --sky:#1aa6e2;
    --sky-pale:#a9def4;
    --ink:#2b2b2b;
    --grey:#4a4a4a;
    --band:#161616;
    --white:#ffffff;
    --stage:#d6d6d6;
  }
  *{margin:0;padding:0;box-sizing:border-box}
  html,body{width:900px;height:1200px;overflow:hidden;background:var(--stage)}
  .flyer{position:absolute;left:64px;top:57px;width:774px;height:1085px;background:var(--white);overflow:hidden;font-family:"PT Sans",sans-serif}
  .flyer-art{position:absolute;inset:0}
  .brand{position:absolute;left:34px;top:34px;display:flex;align-items:center;gap:8px}
  .brand-dot{width:66px;height:66px;border-radius:50%;background:var(--purple)}
  .brand-name{font-family:"Montserrat",sans-serif;font-weight:400;font-size:26px;color:var(--purple);line-height:1}
  .headline{position:absolute;left:36px;top:166px;font-family:"Montserrat",sans-serif}
  .headline-main{font-weight:700;font-size:40px;color:var(--purple);letter-spacing:.5px;line-height:1.05}
  .headline-sub{font-weight:400;font-size:20px;color:var(--grey);letter-spacing:.3px;margin-top:4px}
  .credential{position:absolute;left:36px;top:244px;font-family:"Roboto Condensed",sans-serif;font-weight:700}
  .credential-title{font-size:30px;color:var(--purple);line-height:1.25}
  .credential-years{font-size:22px;color:var(--ink);line-height:1.3}
  .intro{position:absolute;left:207px;top:586px;width:540px;text-align:center;font-family:"Arimo",sans-serif;font-weight:700}
  .intro-lead{font-size:20px;color:var(--sky);line-height:1.2}
  .intro-rest{font-size:15px;color:var(--white);margin-top:5px}
  .services{position:absolute;left:218px;top:670px;width:428px;list-style:none;font-weight:700;font-size:13.6px;line-height:19px;color:var(--ink);text-align:justify}
  .services li{position:relative;padding-left:28px;margin-bottom:16px}
  .services li::before{content:"";position:absolute;left:0;top:4px;width:12px;height:12px;border-radius:50%;background:var(--sky)}
  .footer{position:absolute;left:0;bottom:0;width:774px;height:64px;background:var(--band);color:var(--white);font-family:"Arimo",sans-serif}
  .footer-brand{position:absolute;left:44px;top:18px;display:flex;align-items:center;gap:6px;font-size:19px}
  .footer-brand span.dot{width:22px;height:22px;border-radius:50%;background:var(--white)}
  .contact{position:absolute;display:flex;align-items:center;gap:8px;font-size:16px}
  .contact svg{width:14px;height:14px;fill:var(--sky)}
  .contact-phone{left:220px;top:8px}
  .contact-mail{left:220px;top:32px}
  .contact-web{left:488px;top:10px}
</style>
</head>
<body>
<div class="flyer">
  <svg class="flyer-art" viewBox="0 0 774 1085" width="774" height="1085">
    <defs>
      <linearGradient id="skyFill" x1="0" y1="0" x2="0.3" y2="1">
        <stop offset="0" stop-color="#ffffff"/>
        <stop offset=".35" stop-color="#c6eaf8"/>
        <stop offset="1" stop-color="#7fcdef"/>
      </linearGradient>
      <linearGradient id="bodyTone" x1="0" y1="0" x2="1" y2="1">
        <stop offset="0" stop-color="#f4f4f4"/>
        <stop offset=".5" stop-color="#e6c2a8"/>
        <stop offset="1" stop-color="#f2f2f2"/>
      </linearGradient>
      <linearGradient id="waistTone" x1="0" y1="0" x2="0" y2="1">
        <stop offset="0" stop-color="#5fc2e8"/>
        <stop offset=".3" stop-color="#e2b08c"/>
        <stop offset=".7" stop-color="#d99b73"/>
        <stop offset="1" stop-color="#5cbfe6"/>
      </linearGradient>
      <linearGradient id="faceTone" x1="0" y1="0" x2="1" y2="0">
        <stop offset="0" stop-color="#ffffff" stop-opacity="0"/>
        <stop offset="1" stop-color="#c9d7e0"/>
      </linearGradient>
      <clipPath id="heroClip"><circle cx="625" cy="248" r="252"/></clipPath>
      <clipPath id="portraitClip"><circle cx="149" cy="473" r="80"/></clipPath>
    </defs>

    <rect class="backdrop-face" x="430" y="520" width="344" height="500" fill="url(#faceTone)" role="img" aria-label="Faint close-up portrait in cool tones"/>

    <path class="sky-panel" d="M0,150 Q230,122 440,135 Q360,300 390,470 Q220,520 0,690 Z" fill="url(#skyFill)"/>
    <path class="sky-rule" d="M0,150 Q230,122 440,135" fill="none" stroke="var(--purple)" stroke-width="4"/>

    <rect x="360" y="-10" width="420" height="520" fill="url(#bodyTone)" clip-path="url(#heroClip)" role="img" aria-label="Woman in light sports top showing a slim waist"/>
    <circle cx="625" cy="248" r="259" fill="none" stroke="var(--sky)" stroke-width="12"/>
    <circle cx="625" cy="248" r="270" fill="none" stroke="var(--purple)" stroke-width="5"/>

    <circle cx="149" cy="473" r="80" fill="#e3dcd6" role="img" aria-label="Before and after facial rejuvenation portrait"/>
    <rect x="149" y="390" width="80" height="170" fill="#cfc4bb" clip-path="url(#portraitClip)"/>
    <circle cx="149" cy="473" r="86" fill="none" stroke="var(--purple)" stroke-width="7"/>

    <path class="waist-photo" d="M0,700 Q60,664 120,676 L168,1021 L0,1021 Z" fill="url(#waistTone)" role="img" aria-label="Toned waist in blue briefs"/>
    <path d="M122,676 L170,1021" stroke="var(--sky)" stroke-width="6" fill="none"/>
    <path d="M131,672 L180,1021" stroke="var(--purple)" stroke-width="4" fill="none"/>

    <path class="sweep" d="M90,640 Q330,470 774,500" fill="none" stroke="var(--sky)" stroke-width="8"/>
    <path class="sweep" d="M80,652 Q320,484 774,516" fill="none" stroke="var(--purple)" stroke-width="4"/>

    <path class="intro-band" d="M221,573 H724 a30,30 0 0 1 30,30 V653 H221 a30,40 0 0 1 0,-80 Z" fill="var(--band)"/>
  </svg>

  <div class="brand"><span class="brand-dot"></span><span class="brand-name">Harbor Renewals</span></div>

  <div class="headline">
    <div class="headline-main">GET THE BODY</div>
    <div class="headline-sub">YOU HAVE ALWAYS WANTED</div>
  </div>

  <div class="credential">
    <div class="credential-title">Board certified physician</div>
    <div class="credential-years">With over 20 years of experience</div>
  </div>

  <div class="intro">
    <div class="intro-lead">We assist our clients in naturally optimizing</div>
    <div class="intro-rest">their wellness and appearancethrough a holistic approach which includes</div>
  </div>

  <ul class="services">
    <li>A personalized, medically-supervised weight loss program,</li>
    <li>Cosmetic body treatments such as lipolaser, cool sculpting, radio frequency and ultrasound cavitation, skin tightening, lifting.</li>
    <li>We can reduce double chin, acne scars, facial wrinkles and blemishes.</li>
    <li>Our state of the art machines can reduce cellulite. and skin dimpling physician-formulated vitamins, supplements, nutraceuticals and skin care products which will be offered in our medical offices and online nationally.</li>
    <li>vitamin and mineral-enhanced beverage products which will also be offered in our offices as well as online nationally. We want our improve the way our clients feel, as well as how they look.</li>
  </ul>

  <footer class="footer">
    <div class="footer-brand"><span class="dot"></span>Harbor Renewals</div>
    <div class="contact contact-phone">
      <svg viewBox="0 0 24 24"><path d="M6.6 10.8a15 15 0 0 0 6.6 6.6l2.2-2.2c.3-.3.7-.4 1-.2 1.1.4 2.3.6 3.6.6.6 0 1 .4 1 1V20c0 .6-.4 1-1 1A17 17 0 0 1 3 4c0-.6.4-1 1-1h3.5c.6 0 1 .4 1 1 0 1.3.2 2.5.6 3.6.1.3 0 .7-.2 1z"/></svg>
      (555) 014-2290
    </div>
    <div class="contact contact-mail">
      <svg viewBox="0 0 24 24"><path d="M2 5h20v14H2z M2 5l10 8 10-8" stroke="#161616" stroke-width="1.5"/></svg>
      hello@harborrenewals.net
    </div>
    <div class="contact contact-web">
      <svg viewBox="0 0 24 24"><circle cx="12" cy="12" r="10"/><path d="M2 12h20M12 2c3 3 3 17 0 20M12 2c-3 3-3 17 0 20" stroke="#161616" stroke-width="1.4" fill="none"/></svg>
      www.harborrenewals.net
    </div>
  </footer>
</div>
</body>
</html>
```